New website for Holloway Law Firm at www.keepfirmplan.example

We are a professional law firm located in the Nashville, Tennessee USA area. We focus on personal injury law. We are looking for a slick new website that is user friendly for updating with new blogs, videos, etc. The primary colors should be red, black, and white. It should load extremely fast and have a good mobile component. The pages for the design will include a home page, about us, news, contact us, and practice page. The practice page will be copied for all the practice areas including motor vehicle accidents, slip and fall accidents, dog bites, etc. We have included an image which we would like to include in the new site which shows the color scheme The image is called banner-Car Wreck. The new website should NOT have gavels, court houses, law books, scales or the typical images for a law firm.

Target Market(s)

People in Tennessee involved in accidents

Industry/Entity Type

Legal services, law firm

Number of Pages Required

5+ page

Font styles to use
Serif

Colors
EB3D1F
EC4F4E
F09395
F8D3D4
FCEDEE

Requirements
Should not have
• Gavels, columns, scales, law related images

```html
<!DOCTYPE html>
<html lang="en">
<head>
<meta charset="utf-8">
<title>Holloway Law Firm – Website Design</title>
<link rel="stylesheet" href="https://fonts.googleapis.com/css2?family=Playfair+Display:wght@400;500;700&family=Poppins:ital,wght@0,400;0,500;0,600;0,700;0,800;1,400;1,800&display=swap">
<style>
:root{
  --board:#6e6d72;
  --red:#c8202a;
  --red-bright:#d3232d;
  --ink:#1c1c1e;
  --dark:#1b1b1d;
  --paper:#ffffff;
  --mist:#f0f0f0;
  --line:#e4e4e4;
  --serif:'Playfair Display', Georgia, serif;
  --sans:'Poppins', Arial, sans-serif;
}
*{margin:0;padding:0;box-sizing:border-box}
html,body{width:1200px;height:3098px;overflow:hidden;background:var(--board)}
.board{position:relative;width:998px;height:2576px;transform:scale(1.2024);transform-origin:0 0;background:var(--board);font-family:var(--sans);color:var(--ink);overflow:hidden}
.board-shapes{position:absolute;inset:0}
.board-title{position:absolute;top:50px;left:0;width:998px;text-align:center;font-family:var(--serif);font-size:52px;font-weight:500;letter-spacing:2px;color:#fff}
.board-label{position:absolute;font-family:var(--sans);font-weight:800;font-size:18.5px;color:#fff}

.frame{position:absolute;width:384px;background:var(--paper);overflow:hidden;box-shadow:0 4px 14px rgba(0,0,0,.25)}
.abs{position:absolute}
.photo{position:absolute}

/* header */
.site-header{position:absolute;top:0;left:0;width:384px;height:27px;background:#fff;z-index:3}
.wordmark{position:absolute;font-family:var(--serif);font-weight:400;color:var(--red);white-space:nowrap;line-height:1}
.site-header .wordmark{left:28px;top:10px;font-size:7.5px}
.nav{position:absolute;left:158px;top:11.5px;display:flex;gap:6.5px;font-size:3.3px;font-weight:500;color:#333}
.nav span{position:relative}
.nav .on{color:var(--red)}
.nav .on::before{content:"";position:absolute;left:0;right:0;top:-11.5px;height:1.5px;background:var(--red)}
.call{position:absolute;left:296px;top:7px;display:flex;align-items:center;gap:3px}
.call-icon{width:11px;height:11px;background:var(--red);border-radius:1px;display:flex;align-items:center;justify-content:center}
.call small{display:block;font-size:2.4px;color:#666;letter-spacing:.2px}
.call b{display:block;font-size:4.6px;font-weight:700}

/* banner */
.page-banner{position:absolute;top:27px;left:0;width:384px;height:64px;background:var(--mist)}
.page-banner h1{position:absolute;left:0;width:384px;top:22px;text-align:center;font-family:var(--serif);font-weight:400;font-size:16px}
.page-banner .photo{right:0;top:8px;width:80px;height:52px;background:radial-gradient(circle at 55% 55%,#e33a3f 0,#a8141c 35%,rgba(240,240,240,0) 72%)}

/* type */
.eyebrow{font-size:2.7px;font-weight:700;color:var(--red);letter-spacing:.3px;text-transform:uppercase}
.h-serif{font-family:var(--serif);font-weight:400;color:var(--ink)}
.lede{font-size:3.4px;font-weight:600}
.copy{font-size:2.8px;line-height:4.4px;color:#555}
.btn{position:absolute;height:8px;padding:0 6px;display:flex;align-items:center;font-size:2.8px;font-weight:700;color:#fff;background:var(--ink);letter-spacing:.2px;white-space:nowrap}
.btn.red{background:var(--red)}
.vline{position:absolute;width:.6px;background:var(--red)}
.center{text-align:center;left:0;width:384px}

/* cards */
.card{position:absolute;background:#fff;box-shadow:0 1px 4px rgba(0,0,0,.14)}
.card .photo{left:0;top:0;width:100%;height:67px}
.card h3{position:absolute;left:8px;right:6px;top:74px;font-size:3.5px;font-weight:600}
.card p{position:absolute;left:8px;right:6px;top:81px;font-size:2.7px;line-height:3.9px;color:#666}
.card .more{position:absolute;left:8px;top:106px;font-size:2.5px;font-weight:600;color:var(--red);text-decoration:underline}
.card .meta{position:absolute;left:8px;top:72px;font-size:2.3px;color:#888}

/* stats */
.stat{position:absolute;width:60px;text-align:center;color:#fff}
.stat svg{display:block;margin:0 auto}
.stat b{display:block;font-weight:800;font-style:italic;font-size:17px;line-height:20px;margin-top:2px}
.stat span{display:block;font-size:3.4px;font-weight:500}

/* testimonial */
.quote-mark{position:absolute;font-family:var(--serif);font-size:44px;line-height:1;color:#e6e6e6}
.avatar{position:absolute;width:36px;height:36px;border-radius:50%;border:2px solid #fff;box-shadow:0 1px 5px rgba(0,0,0,.2)}
.testimonial{position:absolute;width:104px;font-size:3.1px;line-height:4.6px;font-style:italic;color:#555}
.testimonial b{display:block;font-style:normal;font-size:2.8px;color:var(--ink);margin-top:3px}

/* appointment */
.appt{position:absolute;left:0;width:384px;height:173px;background:#fff;overflow:hidden}
.appt-form{position:absolute;left:0;top:0;width:204px;height:173px;background:var(--red-bright)}
.field{position:absolute;height:11px;background:#fff;font-size:2.7px;color:#777;padding:3.5px 4px}
.appt h2{position:absolute;left:226px;top:20px;font-family:var(--serif);font-weight:400;line-height:1;color:var(--ink)}
.appt h2 span{display:block;font-size:13px}
.appt h2 strong{display:block;font-weight:400;font-size:20px;margin-top:1px}
.appt .copy{position:absolute;left:226px;top:60px;width:128px}
.appt .photo{right:0;bottom:0;width:104px;height:80px;background:radial-gradient(ellipse at 65% 65%,#e84046 0,#a5121b 32%,#3a0b0e 52%,rgba(255,255,255,0) 74%)}

/* footer */
.site-footer{position:absolute;left:0;width:384px;height:158px;background:var(--dark);color:#fff}
.site-footer .wordmark{left:28px;top:64px;font-size:8.5px}
.f-col{position:absolute;top:38px}
.f-col h4{font-size:4.4px;font-weight:500;margin-bottom:6px}
.f-col li{list-style:none;font-size:2.9px;color:#ccc;line-height:10px}
.f-item{display:flex;gap:3px;font-size:2.8px;color:#ccc;line-height:3.9px;margin-bottom:4px;white-space:nowrap}
.f-item i{display:block;width:3px;height:3px;background:var(--red);border-radius:50%;margin-top:.6px;flex:none}
.f-item b{display:block;color:#fff;font-weight:500}
.news-input{position:absolute;top:68px;left:0;width:83px;height:10px;background:#fff;font-size:2.7px;color:#777;padding:3.5px 4px}
.news-input em{position:absolute;right:0;top:0;width:10px;height:10px;background:var(--red);display:flex;align-items:center;justify-content:center}
.socials{position:absolute;top:92px;left:4px;display:flex;gap:5px}
.socials span{width:8px;height:8px;border-radius:50%;border:.6px solid #777}
.f-bottom{position:absolute;left:0;top:140px;width:384px;border-top:.5px solid #333;text-align:center;font-size:2.6px;font-weight:600;padding-top:6px}
.to-top{position:absolute;right:9px;top:133px;width:9px;height:9px;border-radius:50%;background:#fff;display:flex;align-items:center;justify-content:center}

/* news list */
.post{position:absolute;left:28px;width:244px;height:77px}
.post .photo{left:0;top:0;width:78px;height:77px}
.post .body{position:absolute;left:78px;top:2px;width:166px;height:73px;background:#fff;box-shadow:0 1px 5px rgba(0,0,0,.13);padding:10px 10px 0 11px}
.post .meta{font-size:2.3px;color:#888}
.post h3{font-size:3.6px;font-weight:600;margin:3px 0 3px}
.post p{font-size:2.7px;line-height:3.9px;color:#666}
.post .more{display:block;margin-top:3px;font-size:2.5px;font-weight:600;color:var(--red);text-decoration:underline}
.side h4{font-size:3.6px;font-weight:600;margin-bottom:4px}
.side li{list-style:none;font-size:2.7px;color:#666;line-height:5.3px}
.side .more{font-size:2.7px;color:var(--red);font-weight:600;text-decoration:underline}
.mini{display:flex;gap:3px;margin-bottom:6px}
.mini i{display:block;width:18px;height:18px;flex:none}
.mini span{font-size:2.3px;line-height:3.3px;color:#555}
.mini small{display:block;color:#999}
.pager{position:absolute;display:flex;align-items:center;gap:6px;font-size:3px}
.pager .arrow{width:8px;height:8px;border-radius:50%;background:var(--ink);display:flex;align-items:center;justify-content:center}
.pager .cur{width:7px;height:7px;border-radius:50%;background:var(--red);color:#fff;display:flex;align-items:center;justify-content:center}

/* contact */
.info-box{position:absolute;width:84px;height:61px;background:#fff;box-shadow:0 1px 6px rgba(0,0,0,.14);text-align:center;padding-top:18px}
.info-box .ico{position:absolute;left:34px;top:-13px;width:16px;height:16px;background:var(--ink);display:flex;align-items:center;justify-content:center}
.info-box h4{font-size:3.5px;font-weight:600;margin-bottom:3px}
.info-box p{font-size:2.7px;line-height:4px;color:#666}
</style>
</head>
<body>
<div class="board">
  <svg class="board-shapes" width="998" height="2576" viewBox="0 0 998 2576" aria-hidden="true">
    <polygon points="0,760 998,300 998,1500 0,1900" fill="#737277"/>
    <polygon points="0,1900 998,1500 998,2576 0,2576" fill="#6a696e"/>
    <polygon points="520,2576 998,1950 998,2576" fill="#77767b"/>
  </svg>

  <div class="board-title">HOLLOWAY LAW FIRM</div>
  <div class="board-label" style="left:100px;top:155px">Desktop</div>
  <div class="board-label" style="left:528px;top:155px">About Us</div>
  <div class="board-label" style="left:527px;top:946px">Latest News</div>
  <div class="board-label" style="left:527px;top:1721px">Contact Us</div>
  <div class="board-label" style="left:101px;top:1861px">Practice Areas</div>

  <!-- ================= HOME ================= -->
  <div class="frame home" style="left:102px;top:187px;height:1623px">
    <header class="site-header">
      <div class="wordmark">Holloway Law Firm</div>
      <nav class="nav"><span>HOME</span><span>ABOUT US</span><span>PRACTICES</span><span>NEWS</span><span>CONTACT US</span></nav>
      <div class="call"><span class="call-icon"><svg width="6" height="6" viewBox="0 0 24 24"><path fill="#fff" d="M6.6 10.8a15 15 0 0 0 6.6 6.6l2.2-2.2c.3-.3.7-.4 1-.2 1.1.4 2.3.6 3.6.6.6 0 1 .4 1 1V20c0 .6-.4 1-1 1A17 17 0 0 1 3 4c0-.6.4-1 1-1h3.5c.6 0 1 .4 1 1 0 1.3.2 2.5.6 3.6.1.3 0 .7-.2 1z"/></svg></span><span><small>CALL NOW</small><b>(615) 555-0142</b></span></div>
    </header>

    <section class="hero abs" style="left:0;top:27px;width:384px;height:204px">
      <div class="photo" role="img" aria-label="Close-up of a red car headlight shattering in a collision" style="inset:0;background:linear-gradient(105deg,#0c0c0e 0,#121114 34%,#2c0a0d 52%,#9e1820 70%,#d62a31 80%,#5a0d12 100%)"></div>
      <div class="abs" style="left:28px;top:54px;width:12px;height:.6px;background:var(--red)"></div>
      <div class="abs eyebrow" style="left:45px;top:52.5px;font-size:2.5px">HOLLOWAY LAW FIRM PLLC</div>
      <h1 class="abs" style="left:28px;top:59px;font-family:var(--serif);font-weight:400;color:#fff;font-size:19px;line-height:20px">Don’t lose<br>what’s legally<br>yours</h1>
      <div class="abs" style="left:28px;top:125px;font-size:3.6px;color:#eee">We are trial lawyers and we are proud of it!</div>
      <div class="btn red" style="left:28px;top:140px">BOOK AN APPOINTMENT</div>
      <svg class="abs" style="left:27px;top:180px" width="4" height="8" viewBox="0 0 4 8"><path d="M2 0v7M.5 3.5 2 5l1.5-1.5M.5 5.5 2 7l1.5-1.5" stroke="#fff" stroke-width=".5" fill="none"/></svg>
    </section>

    <section class="about-teaser">
      <div class="abs" style="left:44px;top:318px;width:112px;height:117px;border:6px solid var(--red)"></div>
      <div class="photo" role="img" aria-label="Dog baring its teeth near a person's arm" style="left:70px;top:258px;width:91px;height:95px;background:linear-gradient(135deg,#cfc6bd,#7a6a5c 55%,#3d302a)"></div>
      <div class="photo" role="img" aria-label="Overturned red truck beside the road" style="left:118px;top:323px;width:64px;height:88px;background:linear-gradient(160deg,#d9dcdf,#9da4aa 45%,#a8262c 62%,#6b7066);border:2px solid #fff"></div>
      <div class="vline" style="left:216px;top:245px;height:46px"></div>
      <div class="abs eyebrow" style="left:206px;top:294px">About us</div>
      <h2 class="abs h-serif" style="left:206px;top:301px;font-size:12px">Trial Lawyers...</h2>
      <div class="abs lede" style="left:206px;top:320px">We are trial lawyers and we are proud of it!</div>
      <p class="abs copy" style="left:206px;top:336px;width:136px">There are many law firms in Tennessee who claim to be trial lawyers, but their attorneys have never seen a courtroom. We have tried hundreds of cases to verdict and we have helped thousands of people in the Tennessee courts. We fight against billion dollar insurance companies, billion dollar corporations, and the State of Tennessee, and we win!</p>
      <div class="btn" style="left:206px;top:389px">LEARN MORE</div>
    </section>

    <section class="practice-teaser">
      <div class="abs" style="left:0;top:618px;width:384px;height:118px;background:var(--red-bright)"></div>
      <div class="abs eyebrow center" style="top:461px">Services</div>
      <h2 class="abs h-serif center" style="top:466px;font-size:12px">Practice Areas</h2>
      <div class="abs" style="left:327px;top:467px;width:10px;height:10px;border:.5px solid #333;display:flex;align-items:center;justify-content:center"><svg width="4" height="4" viewBox="0 0 4 4"><path d="M2.6.6 1.2 2l1.4 1.4" stroke="#333" stroke-width=".5" fill="none"/></svg></div>
      <div class="abs" style="left:344px;top:467px;width:10px;height:10px;background:var(--ink);display:flex;align-items:center;justify-content:center"><svg width="4" height="4" viewBox="0 0 4 4"><path d="M1.4.6 2.8 2 1.4 3.4" stroke="#fff" stroke-width=".5" fill="none"/></svg></div>

      <article class="card" style="left:28px;top:495px;width:79px;height:123px"><div class="photo" role="img" aria-label="Red car front crumpling on impact" style="background:linear-gradient(135deg,#1a1a1c,#b81c24 55%,#2a0a0c)"></div><h3>Motor Vehicle Accident</h3><p>Lorem quis bibendum auctor, nisi elit consequat ipsum, nec sagittis sem nibh id elit.</p><span class="more">LEARN MORE</span></article>
      <article class="card" style="left:111px;top:495px;width:79px;height:123px"><div class="photo" role="img" aria-label="Man sitting holding his injured knee" style="background:linear-gradient(135deg,#e8e4df,#8b7d72 50%,#4a3f38)"></div><h3>Personal Injury</h3><p>Lorem quis bibendum auctor, nisi elit consequat ipsum, nec sagittis sem nibh id elit.</p><span class="more">LEARN MORE</span></article>
      <article class="card" style="left:194px;top:495px;width:79px;height:123px"><div class="photo" role="img" aria-label="Woman lying on the ground after a fall" style="background:linear-gradient(135deg,#d7d9dc,#9aa2ab 50%,#6c7885)"></div><h3>Slip and Fall Accident</h3><p>Lorem quis bibendum auctor, nisi elit consequat ipsum, nec sagittis sem nibh id elit.</p><span class="more">LEARN MORE</span></article>
      <article class="card" style="left:277px;top:495px;width:79px;height:123px"><div class="photo" role="img" aria-label="Dog with open mouth outdoors" style="background:linear-gradient(135deg,#b9cfe0,#c9a57a 50%,#7d5a3a)"></div><h3>Dog Bites</h3><p>Lorem quis bibendum auctor, nisi elit consequat ipsum, nec sagittis sem nibh id elit.</p><span class="more">LEARN MORE</span></article>

      <div class="stat" style="left:55px;top:648px"><svg width="20" height="18" viewBox="0 0 20 18" fill="none" stroke="#fff" stroke-width=".8"><rect x="3" y="6" width="14" height="10" rx="1"/><path d="M7 6V3h6v3M3 10h14"/></svg><b>15</b><span>Total Projects</span></div>
      <div class="stat" style="left:128px;top:648px"><svg width="20" height="18" viewBox="0 0 20 18" fill="none" stroke="#fff" stroke-width=".8"><path d="M10 13 5 8a3 3 0 0 1 5-3 3 3 0 0 1 5 3z"/><path d="M3 15h8l4-3"/></svg><b>10</b><span>Happy Clients</span></div>
      <div class="stat" style="left:201px;top:648px"><svg width="20" height="18" viewBox="0 0 20 18" fill="none" stroke="#fff" stroke-width=".8"><circle cx="7" cy="6" r="3"/><circle cx="13" cy="6" r="3"/><path d="M2 16c0-4 3-5 5-5s5 1 5 5M8 16c0-4 3-5 5-5s5 1 5 5"/></svg><b>05</b><span>Team Members</span></div>
      <div class="stat" style="left:274px;top:648px"><svg width="20" height="18" viewBox="0 0 20 18" fill="none" stroke="#fff" stroke-width=".8"><circle cx="10" cy="8" r="6"/><path d="M4 8h12M10 2c2 2 2 10 0 12M10 2c-2 2-2 10 0 12"/></svg><b>100</b><span>Journey Life</span></div>
    </section>

    <section class="video-teaser">
      <div class="photo" role="img" aria-label="Woman holding her head beside a damaged red car" style="left:196px;top:737px;width:188px;height:185px;background:linear-gradient(160deg,#c9ccd1,#8d949c 45%,#3b3e44 62%,#b51d25 80%,#6c1016)"></div>
      <div class="abs" style="left:183px;top:816px;width:26px;height:26px;border-radius:50%;background:#fff;box-shadow:0 1px 5px rgba(0,0,0,.25);display:flex;align-items:center;justify-content:center"><svg width="6" height="6" viewBox="0 0 6 6"><path d="M1.5 .6 5.2 3 1.5 5.4z" fill="#c8202a"/></svg></div>
      <div class="vline" style="left:38px;top:773px;height:28px"></div>
      <div class="abs eyebrow" style="left:28px;top:809px">Video Play</div>
      <h2 class="abs h-serif" style="left:28px;top:816px;font-size:11.5px;line-height:13px">We Are a Professional<br>Law Firm PLLC...</h2>
      <div class="abs lede" style="left:28px;top:859px;font-weight:500">We are trial lawyers and we are proud of it!</div>
      <div class="btn" style="left:28px;top:873px">LEARN MORE</div>
    </section>

    <section class="testimonials">
      <div class="abs eyebrow center" style="top:954px">Testimonials</div>
      <h2 class="abs h-serif center" style="top:959px;font-size:12px">What Our Client Say</h2>
      <div class="quote-mark" style="left:140px;top:984px">“</div>
      <div class="avatar" role="img" aria-label="Client portrait" style="left:40px;top:1010px;background:linear-gradient(135deg,#9b7f6d,#4a3a33)"></div>
      <p class="testimonial" style="left:86px;top:1007px">Speak up for those who cannot speak for themselves, for the rights of all who are destitute. Speak up and judge fairly; defend the rights of the poor and needy.<b>— PROVERBS 31:8-9</b></p>
      <div class="quote-mark" style="left:300px;top:984px">“</div>
      <div class="avatar" role="img" aria-label="Client portrait" style="left:200px;top:1010px;background:linear-gradient(135deg,#8a6a55,#3a2a22)"></div>
      <p class="testimonial" style="left:245px;top:1007px">Speak up for those who cannot speak for themselves, for the rights of all who are destitute. Speak up and judge fairly; defend the rights of the poor and needy.<b>— PROVERBS 31:8-9</b></p>
      <div class="abs" style="left:28px;top:1078px;width:328px;height:.5px;background:var(--line)"></div>
    </section>

    <section class="news-teaser">
      <div class="abs eyebrow center" style="top:1101px">News</div>
      <h2 class="abs h-serif center" style="top:1106px;font-size:12px">The Latest from Holloway</h2>
      <article class="card" style="left:53px;top:1134px;width:90px;height:121px"><div class="photo" role="img" aria-label="Warning triangle on a road in front of a car" style="background:linear-gradient(180deg,#9fb4cc,#4b6584 55%,#b8262d 75%,#3b4656)"></div><span class="meta">by admin · January 2021</span><h3 style="top:78px">Trucking Company Offers 6 Figure Settlement</h3><p style="top:90px">On a Thursday afternoon, our client was traveling to work.</p></article>
      <article class="card" style="left:147px;top:1134px;width:90px;height:121px"><div class="photo" role="img" aria-label="Person slipping on a wet floor" style="background:linear-gradient(160deg,#e6e2dc,#a89f95 55%,#c9a33b 78%,#6b6157)"></div><span class="meta">by admin · January 2021</span><h3 style="top:78px">Holloway Obtains Jury Verdict of 6.1 x Medical Bills</h3><p style="top:90px">In 2016, a client was traveling down a road and stopped in traffic.</p></article>
      <article class="card" style="left:241px;top:1134px;width:90px;height:121px"><div class="photo" role="img" aria-label="Dog pulling on a person's sleeve" style="background:linear-gradient(160deg,#dadcdf,#8f949b 45%,#2a2b30)"></div><span class="meta">by admin · January 2021</span><h3 style="top:78px">Insurance Company Pays for Facial Fractures</h3><p style="top:90px">On a dark night in Larkmont, Tennessee, a young woman.</p></article>
    </section>

    <section class="appt" style="top:1293px">
      <div class="appt-form">
        <div class="field" style="left:34px;top:24px;width:66px">First name</div>
        <div class="field" style="left:103px;top:24px;width:66px">Last name</div>
        <div class="field" style="left:34px;top:40px;width:66px">Phone</div>
        <div class="field" style="left:103px;top:40px;width:66px">Email</div>
        <div class="field" style="left:34px;top:56px;width:66px">Select date</div>
        <div class="field" style="left:103px;top:56px;width:66px">Select time</div>
        <div class="field" style="left:34px;top:70px;width:135px;height:60px">Message</div>
        <div class="btn" style="left:73px;top:139px;height:10px;padding:0 9px">SCHEDULE A CALL</div>
      </div>
      <h2><span>Book An</span><strong>Appointment</strong></h2>
      <p class="copy">Use the form below to tell us about your legal inquiry, and we’ll call you back to schedule an appointment. Please be as detailed as possible. Include what industry you need service for along.</p>
      <div class="photo" role="img" aria-label="Red car front shattering on impact"></div>
    </section>

    <footer class="site-footer" style="top:1466px">
      <div class="wordmark">Holloway Law Firm</div>
      <div class="f-col" style="left:131px"><h4>Quick Links</h4><ul><li>Home</li><li>About us</li><li>Practices Areas</li><li>News</li><li>Contact us</li></ul></div>
      <div class="f-col" style="left:187px"><h4>Contact info</h4><div class="f-item"><i></i><span><b>Email</b>office@hollowaylaw.example</span></div><div class="f-item"><i></i><span><b>Phone</b>(615) 555-0142</span></div><div class="f-item"><i></i><span><b>Location</b>1480 Maple Ridge Drive<br>Suite 210, Cedar Square<br>Larkmont, TN 37000</span></div></div>
      <div class="f-col" style="left:272px"><h4>Newsletter</h4><p class="copy" style="color:#ccc;width:80px">Subscribe to our email address to get the latest news.</p><div class="news-input">Enter Your Email...<em><svg width="4" height="4" viewBox="0 0 4 4"><path d="M.3 2 3.7.3 2.4 3.7 1.8 2.2z" fill="#fff"/></svg></em></div><div class="socials"><span></span><span></span><span></span><span></span></div></div>
      <div class="f-bottom">© 2021 HOLLOWAY LAW FIRM, PLLC . ALL RIGHTS RESERVED.</div>
      <div class="to-top"><svg width="4" height="4" viewBox="0 0 4 4"><path d="M.8 2.6 2 1.4l1.2 1.2" stroke="#222" stroke-width=".5" fill="none"/></svg></div>
    </footer>
  </div>

  <!-- ================= ABOUT ================= -->
  <div class="frame about" style="left:528px;top:187px;height:683px">
    <header class="site-header">
      <div class="wordmark">Holloway Law Firm</div>
      <nav class="nav"><span>HOME</span><span class="on">ABOUT US</span><span>PRACTICES</span><span>NEWS</span><span>CONTACT US</span></nav>
      <div class="call"><span class="call-icon"><svg width="6" height="6" viewBox="0 0 24 24"><path fill="#fff" d="M6.6 10.8a15 15 0 0 0 6.6 6.6l2.2-2.2c.3-.3.7-.4 1-.2 1.1.4 2.3.6 3.6.6.6 0 1 .4 1 1V20c0 .6-.4 1-1 1A17 17 0 0 1 3 4c0-.6.4-1 1-1h3.5c.6 0 1 .4 1 1 0 1.3.2 2.5.6 3.6.1.3 0 .7-.2 1z"/></svg></span><span><small>CALL NOW</small><b>(615) 555-0142</b></span></div>
    </header>
    <div class="page-banner"><h1>About Us</h1><div class="photo" role="img" aria-label="Red car front shattering on impact"></div></div>
    <svg class="abs" style="left:310px;top:110px" width="24" height="30" viewBox="0 0 24 30"><g fill="#222"><circle cx="3" cy="2" r="1.1"/><circle cx="11" cy="2" r="1.1"/><circle cx="19" cy="2" r="1.1"/><circle cx="19" cy="10" r="1.1"/><circle cx="19" cy="18" r="1.1"/><circle cx="19" cy="26" r="1.1"/></g></svg>
    <div class="abs" style="left:28px;top:231px;width:72px;height:75px;border:6px solid var(--red)"></div>
    <div class="photo" role="img" aria-label="Red semi truck cab overturned on a grassy roadside" style="left:59px;top:128px;width:266px;height:148px;background:linear-gradient(170deg,#e4e6e8 0,#b6bcc1 35%,#a6262c 55%,#7b1a1f 65%,#6e7a5a 85%,#4e5a3c)"></div>
    <div class="vline" style="left:192px;top:296px;height:65px"></div>
    <div class="abs eyebrow" style="left:60px;top:330px">About us</div>
    <h2 class="abs h-serif" style="left:60px;top:337px;font-size:12px">Trial Lawyers...</h2>
    <div class="abs lede" style="left:60px;top:355px">We are trial lawyers and we are proud of it!</div>
    <div class="abs copy" style="left:60px;top:372px;width:268px">
      <p style="margin-bottom:4px">There are many law firms in Tennessee who claim to be trial lawyers, but their attorneys have never seen a courtroom. We have tried hundreds of cases to verdict and we have helped thousands of people in the Tennessee courts. We fight against billion dollar insurance companies, billion dollar corporations, and the State of Tennessee, and we win!</p>
      <p style="margin-bottom:4px">It is very hard not to take each case personally. Our clients include victims of personal injury who did not ask for the pain from a car wreck; professionals who are trying to provide for their family and save their license; and parents fighting to keep their children in a child custody proceeding. The majority of our clients are referred by other attorneys because they respect our experience and expertise. Given what is at stake, we take each client’s matter personally and try to work on each case every day in order to bring justice to our clients.</p>
      <p>Our motto is “Don’t Lose What is Legally Yours”. We are the only law firm in Tennessee who has a website like <b style="color:#222">www.keepfirmplan.example</b>. We strive to help our clients and do everything we can to make sure that they don’t lose the money that is owed, don’t lose their license, and don’t lose their family. We cannot make guarantees, however, we can assure every client that we will do everything possible to protect what is theirs.</p>
    </div>
    <div class="btn" style="left:60px;top:479px">MEET THE TEAM</div>
    <footer class="site-footer" style="top:525px">
      <div class="wordmark">Holloway Law Firm</div>
      <div class="f-col" style="left:131px"><h4>Quick Links</h4><ul><li>Home</li><li>About us</li><li>Practices Areas</li><li>News</li><li>Contact us</li></ul></div>
      <div class="f-col" style="left:190px"><h4>Contact info</h4><div class="f-item"><i></i><span><b>Email</b>office@hollowaylaw.example</span></div><div class="f-item"><i></i><span><b>Phone</b>(615) 555-0142</span></div><div class="f-item"><i></i><span><b>Location</b>1480 Maple Ridge Drive<br>Suite 210, Cedar Square<br>Larkmont, TN 37000</span></div></div>
      <div class="f-col" style="left:272px"><h4>Newsletter</h4><p class="copy" style="color:#ccc;width:80px">Subscribe to our email address to get the latest news.</p><div class="news-input">Enter Your Email...<em><svg width="4" height="4" viewBox="0 0 4 4"><path d="M.3 2 3.7.3 2.4 3.7 1.8 2.2z" fill="#fff"/></svg></em></div><div class="socials"><span></span><span></span><span></span><span></span></div></div>
      <div class="f-bottom">© 2021 HOLLOWAY LAW FIRM, PLLC . ALL RIGHTS RESERVED.</div>
      <div class="to-top"><svg width="4" height="4" viewBox="0 0 4 4"><path d="M.8 2.6 2 1.4l1.2 1.2" stroke="#222" stroke-width=".5" fill="none"/></svg></div>
    </footer>
  </div>

  <!-- ================= NEWS ================= -->
  <div class="frame news" style="left:528px;top:979px;height:671px">
    <header class="site-header">
      <div class="wordmark">Holloway Law Firm</div>
      <nav class="nav"><span>HOME</span><span>ABOUT US</span><span>PRACTICES</span><span class="on">NEWS</span><span>CONTACT US</span></nav>
      <div class="call"><span class="call-icon"><svg width="6" height="6" viewBox="0 0 24 24"><path fill="#fff" d="M6.6 10.8a15 15 0 0 0 6.6 6.6l2.2-2.2c.3-.3.7-.4 1-.2 1.1.4 2.3.6 3.6.6.6 0 1 .4 1 1V20c0 .6-.4 1-1 1A17 17 0 0 1 3 4c0-.6.4-1 1-1h3.5c.6 0 1 .4 1 1 0 1.3.2 2.5.6 3.6.1.3 0 .7-.2 1z"/></svg></span><span><small>CALL NOW</small><b>(615) 555-0142</b></span></div>
    </header>
    <div class="page-banner"><h1>Latest News</h1><div class="photo" role="img" aria-label="Red car front shattering on impact"></div></div>

    <article class="post" style="top:120px"><div class="photo" role="img" aria-label="Warning triangle on a road in front of a car" style="background:linear-gradient(180deg,#9fb4cc,#4b6584 55%,#b8262d 75%,#3b4656)"></div><div class="body"><div class="meta">By admin · January 2021</div><h3>Trucking Company Offers 6 Figure Settlement</h3><p>On a Thursday afternoon, our client was traveling to work when suddenly a semi-truck ran through a stop sign and crashed into the side of our client’s truck causing him...</p><span class="more">LEARN MORE</span></div></article>
    <article class="post" style="top:203px"><div class="photo" role="img" aria-label="Injured man lying on a road" style="background:linear-gradient(150deg,#b9bfc6,#5e6b7d 55%,#2a3140)"></div><div class="body"><div class="meta">By admin · January 2021</div><h3>Agency Chooses to Dismiss Case</h3><p>In a case in Larkmont County, the state child welfare office was contacted with claims of abuse to a child by her father. The odd thing was that the claims came only after...</p><span class="more">LEARN MORE</span></div></article>
    <article class="post" style="top:286px"><div class="photo" role="img" aria-label="Dog baring its teeth near a person's arm" style="background:linear-gradient(135deg,#cfc6bd,#7a6a5c 55%,#3d302a)"></div><div class="body"><div class="meta">By admin · January 2021</div><h3>Holloway Obtains Jury Verdict of 6.1 x Medical Bills</h3><p>In 2016, a client was traveling down a road and stopped in traffic when she was hit by another driver in the rear end. Although she thought she was okay, she immediately began...</p><span class="more">LEARN MORE</span></div></article>
    <article class="post" style="top:368px"><div class="photo" role="img" aria-label="Red car front shattering on impact" style="background:linear-gradient(135deg,#1a1a1c,#b81c24 55%,#2a0a0c)"></div><div class="body"><div class="meta">By admin · January 2021</div><h3>Insurance Company Pays for Facial Fractures</h3><p>On a dark night in Larkmont, Tennessee, a young woman was riding in the car with her friends when the driver decided to try to spin the car to make doughnuts. Unfortunately...</p><span class="more">LEARN MORE</span></div></article>

    <aside class="side abs" style="left:287px;top:120px;width:68px">
      <h4>Search</h4>
      <div style="height:9px;border:.5px solid #ddd;font-size:2.5px;color:#999;padding:2.5px 3px;margin-bottom:8px">Search our store</div>
      <h4>Categories</h4>
      <ul style="margin-bottom:2px"><li>Motor vehicle accidents</li><li>Dog bites</li><li>Slip and fall accidents</li><li>Personal injury</li></ul>
      <span class="more">More</span>
      <h4 style="margin-top:14px;margin-bottom:7px">Recent Articles</h4>
      <div class="mini"><i role="img" aria-label="Red car front on impact" style="background:linear-gradient(135deg,#1a1a1c,#b81c24)"></i><span><small>09-02-2021</small>Insurance Company Pays for Facial...</span></div>
      <div class="mini"><i role="img" aria-label="Dog near a person's arm" style="background:linear-gradient(135deg,#cfc6bd,#5d4e43)"></i><span><small>09-02-2021</small>Holloway Obtains Jury Verdict of...</span></div>
      <div class="mini"><i role="img" aria-label="Injured man on a road" style="background:linear-gradient(135deg,#b9bfc6,#3e4a5a)"></i><span><small>09-02-2021</small>Agency Chooses to Dismiss Case</span></div>
      <span class="more">More</span>
    </aside>

    <div class="pager" style="left:28px;top:465px">
      <span class="arrow"><svg width="3" height="3" viewBox="0 0 4 4"><path d="M2.6.6 1.2 2l1.4 1.4" stroke="#fff" stroke-width=".7" fill="none"/></svg></span>
      <span style="margin-left:5px">1</span><span>2</span><span class="cur">3</span><span>4</span><span>9</span>
      <span class="arrow" style="margin-left:5px"><svg width="3" height="3" viewBox="0 0 4 4"><path d="M1.4.6 2.8 2 1.4 3.4" stroke="#fff" stroke-width=".7" fill="none"/></svg></span>
    </div>

    <footer class="site-footer" style="top:514px">
      <div class="wordmark">Holloway Law Firm</div>
      <div class="f-col" style="left:131px"><h4>Quick Links</h4><ul><li>Home</li><li>About us</li><li>Practices Areas</li><li>News</li><li>Contact us</li></ul></div>
      <div class="f-col" style="left:186px"><h4>Contact info</h4><div class="f-item"><i></i><span><b>Email</b>office@hollowaylaw.example</span></div><div class="f-item"><i></i><span><b>Phone</b>(615) 555-0142</span></div><div class="f-item"><i></i><span><b>Location</b>1480 Maple Ridge Drive<br>Suite 210, Cedar Square<br>Larkmont, TN 37000</span></div></div>
      <div class="f-col" style="left:272px"><h4>Newsletter</h4><p class="copy" style="color:#ccc;width:80px">Subscribe to our email address to get the latest news.</p><div class="news-input">Enter Your Email...<em><svg width="4" height="4" viewBox="0 0 4 4"><path d="M.3 2 3.7.3 2.4 3.7 1.8 2.2z" fill="#fff"/></svg></em></div><div class="socials"><span></span><span></span><span></span><span></span></div></div>
      <div class="f-bottom">© 2021 HOLLOWAY LAW FIRM, PLLC . ALL RIGHTS RESERVED.</div>
      <div class="to-top"><svg width="4" height="4" viewBox="0 0 4 4"><path d="M.8 2.6 2 1.4l1.2 1.2" stroke="#222" stroke-width=".5" fill="none"/></svg></div>
    </footer>
  </div>

  <!-- ================= CONTACT ================= -->
  <div class="frame contact" style="left:528px;top:1755px;height:741px">
    <header class="site-header">
      <div class="wordmark">Holloway Law Firm</div>
      <nav class="nav"><span>HOME</span><span>ABOUT US</span><span>PRACTICES</span><span>NEWS</span><span class="on">CONTACT US</span></nav>
      <div class="call"><span class="call-icon"><svg width="6" height="6" viewBox="0 0 24 24"><path fill="#fff" d="M6.6 10.8a15 15 0 0 0 6.6 6.6l2.2-2.2c.3-.3.7-.4 1-.2 1.1.4 2.3.6 3.6.6.6 0 1 .4 1 1V20c0 .6-.4 1-1 1A17 17 0 0 1 3 4c0-.6.4-1 1-1h3.5c.6 0 1 .4 1 1 0 1.3.2 2.5.6 3.6.1.3 0 .7-.2 1z"/></svg></span><span><small>CALL NOW</small><b>(615) 555-0142</b></span></div>
    </header>
    <div class="page-banner"><h1>Contact Us</h1><div class="photo" role="img" aria-label="Red car front shattering on impact"></div></div>
    <div class="abs eyebrow" style="left:59px;top:145px">Holloway</div>
    <h2 class="abs h-serif" style="left:59px;top:151px;font-size:12px">Contact Us</h2>
    <p class="abs copy" style="left:59px;top:176px;width:142px">If you are dealing with a loss caused by someone else, you do not deserve the headache and heartache involved. You should not lose what is legally yours and you need an attorney to make sure that does not happen.</p>
    <div class="abs" style="left:250px;top:165px;width:74px;height:90px;border:5px solid var(--red)"></div>
    <div class="photo" role="img" aria-label="Attorney in a suit talking with a client at a desk" style="left:212px;top:120px;width:92px;height:115px;background:linear-gradient(150deg,#dfe6ee,#8ea4bd 45%,#3a4d66 75%,#1f2a3a)"></div>

    <div class="info-box" style="left:54px;top:309px"><span class="ico"><svg width="7" height="7" viewBox="0 0 24 24"><path fill="#fff" d="M12 2a7 7 0 0 0-7 7c0 5 7 13 7 13s7-8 7-13a7 7 0 0 0-7-7zm0 9.5A2.5 2.5 0 1 1 12 6.5a2.5 2.5 0 0 1 0 5z"/></svg></span><h4>Locations</h4><p>1480 Maple Ridge Drive<br>Suite 210, Cedar Square<br>Larkmont, TN 37000</p></div>
    <div class="info-box" style="left:149px;top:309px"><span class="ico"><svg width="7" height="7" viewBox="0 0 24 24" fill="none" stroke="#fff" stroke-width="2.5"><circle cx="12" cy="12" r="9"/><path d="M12 7v5l3 2"/></svg></span><h4>Office Hours</h4><p>Monday – Friday<br>9AM – 5PM</p></div>
    <div class="info-box" style="left:243px;top:309px"><span class="ico"><svg width="7" height="7" viewBox="0 0 24 24"><path fill="#fff" d="M6.6 10.8a15 15 0 0 0 6.6 6.6l2.2-2.2c.3-.3.7-.4 1-.2 1.1.4 2.3.6 3.6.6.6 0 1 .4 1 1V20c0 .6-.4 1-1 1A17 17 0 0 1 3 4c0-.6.4-1 1-1h3.5c.6 0 1 .4 1 1 0 1.3.2 2.5.6 3.6.1.3 0 .7-.2 1z"/></svg></span><h4>Contact Us</h4><p>office@hollowaylaw.example<br>Phone: (615) 555-0142<br>Fax: (615) 555-0199</p></div>

    <section class="appt" style="top:411px">
      <div class="appt-form">
        <div class="field" style="left:35px;top:24px;width:66px">First name</div>
        <div class="field" style="left:103px;top:24px;width:66px">Last name</div>
        <div class="field" style="left:35px;top:40px;width:66px">Phone</div>
        <div class="field" style="left:103px;top:40px;width:66px">Email</div>
        <div class="field" style="left:35px;top:56px;width:66px">Select date</div>
        <div class="field" style="left:103px;top:56px;width:66px">Select time</div>
        <div class="field" style="left:35px;top:70px;width:134px;height:60px">Message</div>
        <div class="btn" style="left:73px;top:139px;height:10px;padding:0 9px">SCHEDULE A CALL</div>
      </div>
      <h2><span>Book An</span><strong>Appointment</strong></h2>
      <p class="copy">Use the form below to tell us about your legal inquiry, and we’ll call you back to schedule an appointment. Please be as detailed as possible. Include what industry you need service for along.</p>
      <div class="photo" role="img" aria-label="Red car front shattering on impact"></div>
    </section>

    <footer class="site-footer" style="top:583px">
      <div class="wordmark">Holloway Law Firm</div>
      <div class="f-col" style="left:131px"><h4>Quick Links</h4><ul><li>Home</li><li>About us</li><li>Practices Areas</li><li>News</li><li>Contact us</li></ul></div>
      <div class="f-col" style="left:186px"><h4>Contact info</h4><div class="f-item"><i></i><span><b>Email</b>office@hollowaylaw.example</span></div><div class="f-item"><i></i><span><b>Phone</b>(615) 555-0142</span></div><div class="f-item"><i></i><span><b>Location</b>1480 Maple Ridge Drive<br>Suite 210, Cedar Square<br>Larkmont, TN 37000</span></div></div>
      <div class="f-col" style="left:272px"><h4>Newsletter</h4><p class="copy" style="color:#ccc;width:80px">Subscribe to our email address to get the latest news.</p><div class="news-input">Enter Your Email...<em><svg width="4" height="4" viewBox="0 0 4 4"><path d="M.3 2 3.7.3 2.4 3.7 1.8 2.2z" fill="#fff"/></svg></em></div><div class="socials"><span></span><span></span><span></span><span></span></div></div>
      <div class="f-bottom">© 2021 HOLLOWAY LAW FIRM, PLLC . ALL RIGHTS RESERVED.</div>
      <div class="to-top"><svg width="4" height="4" viewBox="0 0 4 4"><path d="M.8 2.6 2 1.4l1.2 1.2" stroke="#222" stroke-width=".5" fill="none"/></svg></div>
    </footer>
  </div>

  <!-- ================= PRACTICE AREAS ================= -->
  <div class="frame practices" style="left:102px;top:1895px;height:601px">
    <header class="site-header">
      <div class="wordmark">Holloway Law Firm</div>
      <nav class="nav"><span>HOME</span><span>ABOUT US</span><span class="on">PRACTICES</span><span>NEWS</span><span>CONTACT US</span></nav>
      <div class="call"><span class="call-icon"><svg width="6" height="6" viewBox="0 0 24 24"><path fill="#fff" d="M6.6 10.8a15 15 0 0 0 6.6 6.6l2.2-2.2c.3-.3.7-.4 1-.2 1.1.4 2.3.6 3.6.6.6 0 1 .4 1 1V20c0 .6-.4 1-1 1A17 17 0 0 1 3 4c0-.6.4-1 1-1h3.5c.6 0 1 .4 1 1 0 1.3.2 2.5.6 3.6.1.3 0 .7-.2 1z"/></svg></span><span><small>CALL NOW</small><b>(615) 555-0142</b></span></div>
    </header>
    <div class="page-banner"><h1>Practice Areas</h1><div class="photo" role="img" aria-label="Red car front shattering on impact"></div></div>

    <article class="card" style="left:48px;top:125px;width:92px;height:123px"><div class="photo" role="img" aria-label="Red car front crumpling on impact" style="background:linear-gradient(135deg,#1a1a1c,#b81c24 55%,#2a0a0c)"></div><h3>Motor Vehicle Accident</h3><p>Lorem quis bibendum auctor, nisi elit consequat ipsum, nec sagittis sem nibh id elit.</p><span class="more">LEARN MORE</span></article>
    <article class="card" style="left:146px;top:125px;width:92px;height:123px"><div class="photo" role="img" aria-label="Man sitting holding his injured knee" style="background:linear-gradient(135deg,#e8e4df,#8b7d72 50%,#4a3f38)"></div><h3>Personal Injury</h3><p>Lorem quis bibendum auctor, nisi elit consequat ipsum, nec sagittis sem nibh id elit.</p><span class="more">LEARN MORE</span></article>
    <article class="card" style="left:244px;top:125px;width:92px;height:123px"><div class="photo" role="img" aria-label="Person slipping on a wet floor" style="background:linear-gradient(160deg,#c8d3de,#8d9aa8 50%,#c9a33b 78%,#6b6157)"></div><h3>Slip and Fall Accident</h3><p>Lorem quis bibendum auctor, nisi elit consequat ipsum, nec sagittis sem nibh id elit.</p><span class="more">LEARN MORE</span></article>
    <article class="card" style="left:48px;top:255px;width:92px;height:123px"><div class="photo" role="img" aria-label="Dog with open mouth outdoors" style="background:linear-gradient(135deg,#b9cfe0,#c9a57a 50%,#7d5a3a)"></div><h3>Dog Bites</h3><p>Lorem quis bibendum auctor, nisi elit consequat ipsum, nec sagittis sem nibh id elit.</p><span class="more">LEARN MORE</span></article>
    <article class="card" style="left:146px;top:255px;width:92px;height:123px"><div class="photo" role="img" aria-label="Pedestrian lying on a crosswalk" style="background:linear-gradient(135deg,#dcdee1,#9ea4ac 50%,#4f5660)"></div><h3>Pedestrian Accidents</h3><p>Lorem quis bibendum auctor, nisi elit consequat ipsum, nec sagittis sem nibh id elit.</p><span class="more">LEARN MORE</span></article>
    <article class="card" style="left:244px;top:255px;width:92px;height:123px"><div class="photo" role="img" aria-label="Wet floor sign in a hallway" style="background:linear-gradient(135deg,#efe7d6,#d4b55c 50%,#9a7b45)"></div><h3>Premises Liability</h3><p>Lorem quis bibendum auctor, nisi elit consequat ipsum, nec sagittis sem nibh id elit.</p><span class="more">LEARN MORE</span></article>

    <div class="btn" style="left:173px;top:394px">LOAD MORE</div>

    <footer class="site-footer" style="top:443px">
      <div class="wordmark">Holloway Law Firm</div>
      <div class="f-col" style="left:131px"><h4>Quick Links</h4><ul><li>Home</li><li>About us</li><li>Practices Areas</li><li>News</li><li>Contact us</li></ul></div>
      <div class="f-col" style="left:185px"><h4>Contact info</h4><div class="f-item"><i></i><span><b>Email</b>office@hollowaylaw.example</span></div><div class="f-item"><i></i><span><b>Phone</b>(615) 555-0142</span></div><div class="f-item"><i></i><span><b>Location</b>1480 Maple Ridge Drive<br>Suite 210, Cedar Square<br>Larkmont, TN 37000</span></div></div>
      <div class="f-col" style="left:272px"><h4>Newsletter</h4><p class="copy" style="color:#ccc;width:80px">Subscribe to our email address to get the latest news.</p><div class="news-input">Enter Your Email...<em><svg width="4" height="4" viewBox="0 0 4 4"><path d="M.3 2 3.7.3 2.4 3.7 1.8 2.2z" fill="#fff"/></svg></em></div><div class="socials"><span></span><span></span><span></span><span></span></div></div>
      <div class="f-bottom">© 2021 HOLLOWAY LAW FIRM, PLLC . ALL RIGHTS RESERVED.</div>
      <div class="to-top"><svg width="4" height="4" viewBox="0 0 4 4"><path d="M.8 2.6 2 1.4l1.2 1.2" stroke="#222" stroke-width=".5" fill="none"/></svg></div>
    </footer>
  </div>
</div>
</body>
</html>
```